Cafe - A FRAME Design

Need to create an A frame for my café.
Logo available
Word document - has basic information we think would be good.

Name: Brovvle Café

Notes from the A-frame printers.
File Requirements
• PDF without trim, crop or registration marks
• All files to be CMYK, not RGB
• All fonts converted to outlines (paths/curves)
• Embed all images and elements
• Files to be 100% scale unless otherwise specified
• 10mm Bleed
Resolution
• Bitmap images no less than 130 DPI at full size
Pantone Colours
• If required Pantone colours must be supplied

Target Market(s)

Mainly Students - University cafe

Requirements
Must have
• Cafe name: Brovvle
Nice to have
• Might be nice to have background - that orange color same as logo - just an idea

Word document - has basic idea regarding text that should be included

```html
<!DOCTYPE html>
<html lang="en">
<head>
<meta charset="utf-8">
<title>Brovvle Café – A-Frame Sign</title>
<link href="https://fonts.googleapis.com/css2?family=Oswald:wght@500&family=Poppins:wght@400;500;600&display=swap" rel="stylesheet">
<style>
  :root {
    --orange-bright: #e55b20;
    --orange-deep: #a9381a;
    --charcoal: #3a3a40;
    --pill: #2c2c31;
    --white: #ffffff;
    --photo-warm: #8a6a52;
    --photo-light: #d9d2c6;
    --photo-dark: #3b2f2a;
  }
  * { margin: 0; padding: 0; box-sizing: border-box; }
  html, body { width: 686px; height: 1200px; overflow: hidden; }
  body { font-family: "Poppins", sans-serif; background: var(--orange-deep); }

  .sign { position: relative; width: 686px; height: 1200px; overflow: hidden; }
  .sign__art { position: absolute; inset: 0; width: 686px; height: 1200px; }

  .brand {
    position: absolute; top: 92px; left: 196px;
    display: flex; align-items: center; gap: 16px;
  }
  .brand__dot { width: 44px; height: 44px; border-radius: 50%; background: var(--orange-bright); }
  .brand__name {
    font-family: "Poppins", sans-serif; font-weight: 600;
    font-size: 58px; line-height: 1; color: var(--charcoal);
  }

  .headline {
    position: absolute; top: 690px; left: 0; width: 686px;
    text-align: center; color: var(--white);
    font-family: "Oswald", sans-serif; font-weight: 500;
    font-size: 47px; line-height: 1.22;
  }

  .offer {
    position: absolute; top: 876px; left: 36px; width: 612px; height: 208px;
    border: 1.5px solid rgba(255,255,255,0.85); border-radius: 10px;
  }
  .offer__divider {
    position: absolute; left: 358px; top: 24px; height: 118px;
    border-left: 2px dotted rgba(255,255,255,0.85);
  }
  .offer__list { position: absolute; top: 24px; list-style: none; }
  .offer__list--left { left: 30px; }
  .offer__list--right { left: 392px; }
  .offer__item {
    display: flex; align-items: center; gap: 14px;
    height: 40px; margin-bottom: 30px;
    color: var(--white); font-size: 24px; font-weight: 500; white-space: nowrap;
  }
  .offer__icon { width: 40px; height: 40px; flex: none; }

  .tagline {
    position: absolute; top: 1057px; left: 126px; width: 432px; height: 46px;
    background: var(--pill); border-radius: 23px;
    box-shadow: 0 8px 10px rgba(60,20,10,0.35);
    color: var(--white); font-family: "Oswald", sans-serif; font-weight: 500;
    font-size: 23px; line-height: 46px; text-align: center; letter-spacing: 0.2px;
  }
  .location {
    position: absolute; top: 1124px; left: 0; width: 686px;
    text-align: center; color: var(--white); font-size: 18px; font-weight: 400;
  }
</style>
</head>
<body>
<main class="sign">
  <svg class="sign__art" viewBox="0 0 686 1200" xmlns="http://www.w3.org/2000/svg">
    <defs>
      <linearGradient id="orangeField" x1="0" y1="0" x2="0" y2="1">
        <stop offset="0.35" stop-color="var(--orange-bright)"/>
        <stop offset="1" stop-color="var(--orange-deep)"/>
      </linearGradient>
      <linearGradient id="photoTone" x1="0" y1="0" x2="1" y2="1">
        <stop offset="0" stop-color="var(--photo-light)"/>
        <stop offset="0.55" stop-color="var(--photo-warm)"/>
        <stop offset="1" stop-color="var(--photo-dark)"/>
      </linearGradient>
    </defs>
    <rect class="sign__field" width="686" height="1200" fill="url(#orangeField)"/>
    <path class="sign__photo" role="img"
          aria-label="Photo: friends chatting over coffee at a café table while a server brings food, brick wall behind"
          fill="url(#photoTone)"
          d="M0,0 H686 V590 C640,575 600,600 560,620 C520,640 490,580 430,600 C380,615 330,680 280,650 C240,625 270,520 200,500 C140,485 80,520 50,480 C20,440 90,360 40,330 C20,318 0,320 0,300 Z"/>
    <path class="sign__wave" fill="none" stroke="var(--white)" stroke-width="16" stroke-linecap="round"
          d="M690,588 C640,575 600,600 560,620 C520,640 490,580 430,600 C380,615 330,680 280,650 C240,625 270,520 200,500 C140,485 80,520 50,480 C20,440 90,360 40,330 C20,318 0,320 -4,300"/>
  </svg>

  <div class="brand">
    <span class="brand__dot"></span>
    <span class="brand__name">Brovvle</span>
  </div>

  <h1 class="headline">Your Environmentally &amp;<br>Sustainability Focused café</h1>

  <section class="offer">
    <ul class="offer__list offer__list--left">
      <li class="offer__item">
        <svg class="offer__icon" viewBox="0 0 40 40" fill="none" stroke="#fff" stroke-width="2">
          <circle cx="20" cy="20" r="18"/>
          <path d="M12 17h13v5a6 6 0 0 1-6 6h-1a6 6 0 0 1-6-6z M25 19h2a2.5 2.5 0 0 1 0 5h-2 M17 10v4 M21 10v4"/>
        </svg>
        Specialty Coffee
      </li>
      <li class="offer__item">
        <svg class="offer__icon" viewBox="0 0 40 40" fill="none" stroke="#fff" stroke-width="2">
          <circle cx="20" cy="20" r="18"/>
          <path d="M13 12h14l-3 10h-8z M20 22v7 M16 29h8 M22 8l-2 6"/>
        </svg>
        Drinks (Vegan &amp; GF)
      </li>
    </ul>
    <div class="offer__divider"></div>
    <ul class="offer__list offer__list--right">
      <li class="offer__item">
        <svg class="offer__icon" viewBox="0 0 40 40" fill="none" stroke="#fff" stroke-width="2">
          <circle cx="20" cy="20" r="18"/>
          <path d="M13 28h14 M14 28v-8h12v8 M14 24h12 M16 20v-6l4-3"/>
        </svg>
        Fresh Food,
      </li>
      <li class="offer__item">
        <svg class="offer__icon" viewBox="0 0 40 40" fill="none" stroke="#fff" stroke-width="2">
          <circle cx="20" cy="20" r="18"/>
          <path d="M11 24c0-6 4-11 9-11s9 5 9 11z M15 24l2-8 M20 24v-10 M25 24l-2-8 M11 28h18"/>
        </svg>
        Pastries
      </li>
    </ul>
  </section>

  <p class="tagline">OPTIONS AVAILABLE CATERING AVAILABLE</p>
  <p class="location">Located @ Building 118</p>
</main>
</body>
</html>
```